educational services
broker of essential services
So I love my Velvet Kettle cards. I love the background.
I like the background on the coral ridge card
I like a little part of each Monarch card
I want my card to stand out and be professional
I would also like somewhat of a brand
I do not want it to be specific to anything but the world and galaxy
I would like to be able to be used for everything, all encompassing
In spanish Sin paredes, not sureother languages but i will do programs for other countries like China, Japan and Korea
Reason: It has been the first week of school and I have not been able to get the feedback I need.
Please change colors to Blue and GOld
Please add ~ over the n in Lorna
Please submit some vertical designs
Please include the world
Please make eagle a watermark
Make sure the Open Horizon doesnt have "preparatory school" under it
I am open to new designs and I will pay more after I chose a designer who seems to get all this stuff in my head!
Reason: Last minute designs were wonderful
Reason: I was out of town and not able to review the wonderful designs posted. I am narrowing the designs down now! I appreciate all the work done thus far.
Hello,
Thank you for all the designs. This is difficult. I have not been able to access them as I was able to last week so please be patient. If you also do web design please send me a message.
Again, thank you. I am down to just a few designs.
Sincerely,
Lorna Vidal Pratchett
I have been extremely busy, I should pick a design by the ned of this week. Thank you for your patience
Business
Dr. Lorna Vidal Pratchett
www.ohacademy-example.com
(555) 284-9071 US
lornajanevidal@mailbox-example.com

```html
<!DOCTYPE html>
<html lang="en">
<head>
<meta charset="utf-8">
<title>Open Horizon – Business Card</title>
<link rel="stylesheet" href="https://fonts.googleapis.com/css2?family=Open+Sans:wght@400;700&display=swap">
<style>
  :root {
    --page: #ececec;
    --card: #f8f1bb;
    --maroon: #5c0b2d;
    --gold: #b2a31a;
    --ink: #3a3a3a;
  }
  html, body {
    margin: 0;
    width: 1200px;
    height: 977px;
    overflow: hidden;
    background: var(--page);
    font-family: "Open Sans", Arial, sans-serif;
  }
  .card {
    position: absolute;
    left: 150px;
    top: 218px;
    width: 900px;
    height: 540px;
    background: var(--card);
    box-shadow: 0 6px 24px rgba(0,0,0,0.12);
    overflow: hidden;
  }
  .band {
    position: absolute;
    height: 30px;
    background: var(--maroon);
    border-radius: 8px;
  }
  .band--top { left: 90px; top: 36px; width: 440px; }
  .band--bottom { left: 430px; top: 472px; width: 410px; }
  .brand {
    position: absolute;
    left: 200px;
    top: 112px;
    display: flex;
    align-items: center;
    gap: 14px;
  }
  .brand__dot {
    width: 64px;
    height: 64px;
    border-radius: 50%;
    background: var(--maroon);
  }
  .brand__name {
    font-size: 56px;
    font-weight: 700;
    color: var(--gold);
    letter-spacing: 1px;
    line-height: 1;
  }
  .holder {
    position: absolute;
    left: 240px;
    top: 232px;
    margin: 0;
    font-size: 30px;
    font-weight: 700;
    color: var(--maroon);
  }
  .contacts {
    position: absolute;
    left: 300px;
    top: 298px;
    margin: 0;
    padding: 0;
    list-style: none;
    font-size: 24px;
    color: var(--ink);
  }
  .contacts li {
    display: flex;
    align-items: center;
    gap: 10px;
    height: 48px;
  }
  .contacts li:nth-child(1) { padding-left: 40px; }
  .contacts li:nth-child(3) { padding-left: 40px; }
  .contacts svg { width: 24px; height: 24px; flex: none; }
</style>
</head>
<body>
  <div class="card">
    <div class="band band--top"></div>

    <div class="brand">
      <span class="brand__dot"></span>
      <span class="brand__name">OPEN HORIZON</span>
    </div>

    <p class="holder">Dr. Lorna Vidal Pratchett</p>

    <ul class="contacts">
      <li>
        <svg viewBox="0 0 24 24" aria-hidden="true">
          <circle cx="12" cy="12" r="11" fill="#2b2b2b"/>
          <path d="M8.5 6.5c.6-.4 1.3-.3 1.6.3l1 1.9c.2.5.1 1-.3 1.3l-.8.6c.5 1.3 1.4 2.3 2.6 2.9l.7-.7c.4-.4.9-.4 1.3-.2l1.9 1c.6.3.7 1 .3 1.6l-.8 1c-.6.7-1.6.9-2.4.5-2.8-1.3-4.8-3.5-5.9-6.3-.3-.9 0-1.8.8-2.4z" fill="#f8f1bb"/>
        </svg>
        <span>(555) 284-9071 US</span>
      </li>
      <li>
        <svg viewBox="0 0 24 24" aria-hidden="true">
          <circle cx="12" cy="12" r="11" fill="#2b2b2b"/>
          <rect x="6" y="8" width="12" height="8.5" rx="1" fill="#f8f1bb"/>
          <path d="M6.5 8.6 12 12.8l5.5-4.2" fill="none" stroke="#2b2b2b" stroke-width="1.2"/>
        </svg>
        <span>lornajanevidal@mailbox-example.com</span>
      </li>
      <li>
        <svg viewBox="0 0 24 24" aria-hidden="true">
          <circle cx="12" cy="12" r="11" fill="#2b2b2b"/>
          <g fill="none" stroke="#f8f1bb" stroke-width="1.2">
            <circle cx="12" cy="12" r="6"/>
            <ellipse cx="12" cy="12" rx="2.6" ry="6"/>
            <path d="M6 12h12"/>
          </g>
        </svg>
        <span>www.ohacademy-example.com</span>
      </li>
    </ul>

    <div class="band band--bottom"></div>
  </div>
</body>
</html>
```